Not another boring Business Card Design Project

This is not another boring Business Card Design Project.

We are looking for the weirdest, wackiest most boundary pushing designs that you can come up with.

If you believe that design can be fun, energetic, crazy, unpredictable, beautiful and eye-catching then read on… this project is for you.

We are Tolvin Presk and we print plastic cards.

We are running a Plastic Card Design Competition.

And we need a plastic card to advertise the competition to graphic designers just like you.

The design needs to make your average designers’ jaws drop and their eyes pop out.

You can do what you wish with the card design, so long as it stands out.

We like these designs, designs that stretch the boundaries and become something beyond just another business card:

http://quorvamedia.net/wp-content/uploads/2009/03/b48.jpg
Designer - http://www.pelvanworks.com/

http://quorvamedia.net/wp-content/uploads/2009/03/b41.jpg
Designer - http://renolbrakstad.com/

http://images.plinthhive.com/designs/44195_732292_37774_thumbnail.jpg
Designer- Zentro Media at Plinth Hive

http://images.plinthhive.com/designs/44195_717529_37774_thumbnail.jpg
Designer - Zentro Media at Plinth Hive

http://quorvamedia.net/wp-content/uploads/2009/03/b11.jpg
Designer - http://www.wk7studio.com/

http://quorvamedia.net/wp-content/uploads/2009/03/b16.jpg
Designer - http://www.pebbletumbler.com/

Reason: A number of designers have said they want to submit designs and haven't yet done so, we want to give them time.

Reason: We've extended the deadline by 4 days for those who want to submit their designs over the weekend and give ourselves time to judge them

Plastic

• The design needs to contain this link: lnk.example/QzRpLk and any other detail that will encourage competition entry. The design will be printed on plastic.
• No borders (when plastic cards are punched to shape and size there is movement of 1 - 2mm, borders highlight this movement).

Keep text 3mm away from edges of the cards.

Please don't create designs to be produced on clear/transparent plastic.

```html
<!DOCTYPE html>
<html lang="en">
<head>
<meta charset="utf-8">
<title>Plastic Card Design Contest</title>
<link rel="stylesheet" href="https://fonts.googleapis.com/css2?family=Courier+Prime:wght@700&family=Arimo:wght@400;700&display=swap">
<style>
  :root {
    --stage: #d6d6d6;
    --card-black: #000000;
    --ink-white: #f4f4f4;
    --glow: rgba(255, 255, 255, 0.5);
    --tone-blue: #4a8fcf;
    --tone-yellow: #d2cf4e;
    --tone-green: #86a55a;
    --tone-pink: #b95a7f;
  }
  html, body {
    margin: 0;
    width: 1200px;
    height: 803px;
    overflow: hidden;
    background: var(--stage);
  }
  .card {
    position: absolute;
    left: 40px;
    top: 36px;
    width: 1120px;
    height: 731px;
    border-radius: 30px;
    background: var(--card-black);
    overflow: hidden;
  }
  .card__artwork {
    position: absolute;
    inset: 0;
  }
  .card__artwork svg {
    width: 100%;
    height: 100%;
    display: block;
  }
  .card__title {
    position: absolute;
    left: 57px;
    top: 375px;
    margin: 0;
    font-family: "Courier Prime", monospace;
    font-weight: 700;
    font-size: 43px;
    letter-spacing: 10.5px;
    line-height: 1;
    color: var(--ink-white);
    text-shadow: 0 0 4px var(--glow);
    white-space: nowrap;
  }
  .card__label {
    position: absolute;
    left: 57px;
    margin: 0;
    font-family: "Arimo", sans-serif;
    font-size: 26px;
    letter-spacing: 3px;
    line-height: 1;
    color: var(--ink-white);
    text-transform: uppercase;
  }
  .card__label--card { top: 421px; }
  .card__label--to { top: 510px; }
  .card__label--participate { top: 547px; }
  .card__link {
    position: absolute;
    left: 294px;
    top: 538px;
    margin: 0;
    font-family: "Courier Prime", monospace;
    font-weight: 700;
    font-size: 40px;
    letter-spacing: 1px;
    line-height: 1;
    color: var(--ink-white);
    text-shadow: 0 0 4px var(--glow);
    white-space: nowrap;
  }
  .card__audience {
    position: absolute;
    left: 46px;
    top: 610px;
    margin: 0;
    font-family: "Arimo", sans-serif;
    font-weight: 700;
    font-size: 56px;
    letter-spacing: 9px;
    line-height: 1;
    color: var(--ink-white);
    text-shadow: 0 0 4px var(--glow);
  }
</style>
</head>
<body>
  <main class="card">
    <div class="card__artwork" role="img" aria-label="Illustration of four overlapping portrait silhouettes in blue, yellow, green and pink with splattered edges">
      <svg viewBox="0 0 1120 731" preserveAspectRatio="none">
        <defs>
          <radialGradient id="tone-blue">
            <stop offset="0" stop-color="var(--tone-blue)" stop-opacity="1"/>
            <stop offset="0.7" stop-color="var(--tone-blue)" stop-opacity="0.9"/>
            <stop offset="1" stop-color="var(--tone-blue)" stop-opacity="0"/>
          </radialGradient>
          <radialGradient id="tone-yellow">
            <stop offset="0" stop-color="var(--tone-yellow)" stop-opacity="1"/>
            <stop offset="0.7" stop-color="var(--tone-yellow)" stop-opacity="0.9"/>
            <stop offset="1" stop-color="var(--tone-yellow)" stop-opacity="0"/>
          </radialGradient>
          <radialGradient id="tone-green">
            <stop offset="0" stop-color="var(--tone-green)" stop-opacity="1"/>
            <stop offset="0.7" stop-color="var(--tone-green)" stop-opacity="0.9"/>
            <stop offset="1" stop-color="var(--tone-green)" stop-opacity="0"/>
          </radialGradient>
          <radialGradient id="tone-pink">
            <stop offset="0" stop-color="var(--tone-pink)" stop-opacity="1"/>
            <stop offset="0.7" stop-color="var(--tone-pink)" stop-opacity="0.9"/>
            <stop offset="1" stop-color="var(--tone-pink)" stop-opacity="0"/>
          </radialGradient>
        </defs>
        <ellipse cx="870" cy="250" rx="250" ry="330" fill="url(#tone-pink)" opacity="0.85"/>
        <ellipse cx="200" cy="330" rx="230" ry="320" fill="url(#tone-blue)" opacity="0.85"/>
        <ellipse cx="420" cy="250" rx="220" ry="300" fill="url(#tone-yellow)" opacity="0.8"/>
        <ellipse cx="640" cy="240" rx="230" ry="320" fill="url(#tone-green)" opacity="0.8"/>
      </svg>
    </div>

    <h1 class="card__title">PLASTIC CARD DESIGN CONTEST</h1>
    <p class="card__label card__label--card">Card</p>
    <p class="card__label card__label--to">To</p>
    <p class="card__label card__label--participate">Participate</p>
    <p class="card__link">lnk.example/QzRpLk</p>
    <p class="card__audience">DESIGNER</p>
  </main>
</body>
</html>
```